Walk Beside The River

Business Card design

Target Market(s)

People who require support in the commnity

Industry/Entity Type

Mental Health Support

Contact Information for Business Card

Mental Health Support Rosalind Tavener walkbesidetheriver@mailbrook.com.au 0458 906 312 PO Box 627 Wattlebrook QLD 4592

Colors
6B429C
8869AF
B7A5CE
E3DAEB
F3F0F8

Requirements
Must have
• Logo & details listed above
Should not have
• No red or orange

```html
<!DOCTYPE html>
<html lang="en">
<head>
<meta charset="utf-8">
<title>Walk Beside The River – Business Card</title>
<link rel="stylesheet" href="https://fonts.googleapis.com/css2?family=Montserrat:wght@500;600;800&display=swap">
<style>
  :root {
    --purple-deep: #6B429C;
    --purple-mid: #8869AF;
    --purple-soft: #B7A5CE;
    --purple-pale: #E3DAEB;
    --purple-mist: #F3F0F8;
    --purple-night: #2E1F5E;
    --sun-yellow: #F1EE5C;
    --card-white: #FFFFFF;
    --backdrop: #ECE8F1;
  }
  * { margin: 0; padding: 0; box-sizing: border-box; }
  html, body { width: 1200px; height: 1000px; overflow: hidden; }
  body {
    background: var(--backdrop);
    font-family: "Montserrat", sans-serif;
    position: relative;
  }
  .card {
    position: absolute;
    width: 600px;
    height: 340px;
    border-radius: 6px;
    box-shadow: 0 14px 34px rgba(46, 31, 94, 0.18);
    overflow: hidden;
  }
  .card--front { left: 50px; top: 110px; background: var(--card-white); }
  .card--back {
    left: 560px; top: 560px;
    background: linear-gradient(160deg, var(--purple-soft) 0%, var(--purple-mid) 32%, var(--purple-deep) 62%, var(--purple-night) 100%);
    display: flex; align-items: center; justify-content: center;
  }
  .brand { display: flex; align-items: center; gap: 12px; }
  .brand__dot { border-radius: 50%; flex: none; }
  .brand__name {
    font-weight: 600;
    letter-spacing: 0.22em;
    text-transform: uppercase;
    line-height: 1.45;
  }
  .card--front .brand { position: absolute; right: 36px; top: 36px; }
  .card--front .brand__dot { width: 24px; height: 24px; background: var(--purple-mid); }
  .card--front .brand__name { color: var(--purple-deep); font-size: 13px; width: 170px; }
  .card--back .brand__dot { width: 28px; height: 28px; background: var(--sun-yellow); }
  .card--back .brand__name { color: var(--card-white); font-size: 18px; width: 250px; }

  .person {
    position: absolute; left: 40px; top: 100px;
    display: inline-flex; flex-direction: column; align-items: flex-end;
  }
  .person__name {
    font-weight: 800;
    font-size: 40px;
    line-height: 1.15;
    color: var(--purple-deep);
    letter-spacing: -0.01em;
  }
  .person__role {
    margin-top: 2px;
    font-weight: 500;
    font-size: 9.5px;
    letter-spacing: 0.2em;
    color: var(--purple-mid);
    text-transform: uppercase;
  }
  .contacts {
    position: absolute; left: 40px; top: 186px;
    list-style: none;
    display: flex; flex-direction: column; gap: 8px;
  }
  .contacts__item {
    display: flex; align-items: center; gap: 14px;
    font-weight: 500;
    font-size: 15px;
    color: var(--purple-deep);
    line-height: 1.25;
  }
  .contacts__icon { width: 18px; height: 18px; flex: none; fill: var(--purple-deep); }
</style>
</head>
<body>

<section class="card card--front" aria-label="Business card front">
  <div class="brand">
    <span class="brand__dot"></span>
    <span class="brand__name">Walk Beside The River</span>
  </div>

  <div class="person">
    <h1 class="person__name">Rosalind Tavener</h1>
    <p class="person__role">Mental Health Support</p>
  </div>

  <ul class="contacts">
    <li class="contacts__item">
      <svg class="contacts__icon" viewBox="0 0 24 24"><path d="M12 2a7 7 0 0 0-7 7c0 5 7 13 7 13s7-8 7-13a7 7 0 0 0-7-7zm0 9.5A2.5 2.5 0 1 1 12 6.5a2.5 2.5 0 0 1 0 5z"/></svg>
      <span>PO Box 627 Wattlebrook<br>QLD 4592</span>
    </li>
    <li class="contacts__item">
      <svg class="contacts__icon" viewBox="0 0 24 24"><path d="M6.6 10.8a15 15 0 0 0 6.6 6.6l2.2-2.2a1 1 0 0 1 1-.25 11.4 11.4 0 0 0 3.6.57 1 1 0 0 1 1 1V20a1 1 0 0 1-1 1A17 17 0 0 1 3 4a1 1 0 0 1 1-1h3.5a1 1 0 0 1 1 1c0 1.25.2 2.45.57 3.57a1 1 0 0 1-.25 1z"/></svg>
      <span>0458 906 312</span>
    </li>
    <li class="contacts__item">
      <svg class="contacts__icon" viewBox="0 0 24 24"><path d="M3 5h18a1 1 0 0 1 1 1v.4l-10 6.2L2 6.4V6a1 1 0 0 1 1-1zm-1 3.7 10 6.2 10-6.2V18a1 1 0 0 1-1 1H3a1 1 0 0 1-1-1z"/></svg>
      <span>walkbesidetheriver@mailbrook.com.au</span>
    </li>
    <li class="contacts__item">
      <svg class="contacts__icon" viewBox="0 0 24 24"><path d="M12 2a10 10 0 1 0 0 20 10 10 0 0 0 0-20zm6.9 6h-2.9a15 15 0 0 0-1.4-3.6A8 8 0 0 1 18.9 8zM12 4a13 13 0 0 1 1.9 4h-3.8A13 13 0 0 1 12 4zM4.3 14a8 8 0 0 1 0-4h3.4a16 16 0 0 0 0 4zm.8 2h2.9a15 15 0 0 0 1.4 3.6A8 8 0 0 1 5.1 16zM8 8H5.1a8 8 0 0 1 4.3-3.6A15 15 0 0 0 8 8zm4 12a13 13 0 0 1-1.9-4h3.8A13 13 0 0 1 12 20zm2.3-6H9.7a14 14 0 0 1 0-4h4.6a14 14 0 0 1 0 4zm.3 5.6A15 15 0 0 0 16 16h2.9a8 8 0 0 1-4.3 3.6zM16.3 14a16 16 0 0 0 0-4h3.4a8 8 0 0 1 0 4z"/></svg>
      <span>walkbesidetheriver@mailbrook.com.au</span>
    </li>
  </ul>
</section>

<section class="card card--back" aria-label="Business card back">
  <div class="brand">
    <span class="brand__dot"></span>
    <span class="brand__name">Walk Beside The River</span>
  </div>
</section>

</body>
</html>
```